Premium stylish simple clever card design for high end construction company.

I need a business card designed that is a standard size and shape (square edges) that is black in colour, with black edges. All text is to be either grey/silver or yellow/gold. On the front I want the logo (supplied as attachment g5) to be embossed or raised to give a texture. I also want the name of my company "The Kestrel Vault (larger font) construction co. (smaller font)" I like the clean style (found in attachment 56419286) of the black background with silver text. But the triangle is to be gold/yellow.

On the back needs to have my contact details. In silver or gold text.

Liam Porter - Builder
Liam@thekestrelvault.com.au
www.thekestrelvault.com.au
0427391065
Lic 517904k
PO BOX 739 Narrabeen NSW 2101

Must look simple, elegant and precise.

My work is of the utmost quality and my business card needs to project that. It needs to be simple and precise. It should scream luxury and confidence. Feel free to get creative with the font and font size. If you google "The Kestrel Vault" you will see it has links to great architecture, art, nature and the fibonacci sequence so i am open to using these ideas also.

Target Market(s)

High End home owners. 30-70 year olds.

Industry/Entity Type

Residential Construction

Contact Information for Business Card

Logo and company name on front. Contact details on back.

Font styles to use
Serif
Sans Serif

Colors
ffcf3e

Requirements
Must have
• black background
Nice to have
• debossed logo (silver and gold)
• debased company name (silver)
Should not have
• It should not look like a standard construction business card with pictures of hammers or tools etc.

```html
<!DOCTYPE html>
<html lang="en">
<head>
<meta charset="utf-8">
<title>The Kestrel Vault — Business Card</title>
<link href="https://fonts.googleapis.com/css2?family=Josefin+Sans:wght@300;400&family=Tinos:wght@400;700&display=swap" rel="stylesheet">
<style>
  :root {
    --backdrop: #dcdcdc;
    --card-black: #050505;
    --gold: #ffcf3e;
    --silver: #9a9a9a;
    --white: #f4f4f4;
    --tone-faint: #151515;
  }
  html, body {
    margin: 0;
    padding: 0;
    width: 1200px;
    height: 900px;
    overflow: hidden;
    background: var(--backdrop);
  }
  .canvas {
    position: relative;
    width: 1200px;
    height: 900px;
  }
  .card {
    position: absolute;
    top: 286px;
    width: 540px;
    height: 328px;
    background: var(--card-black);
    box-shadow: 0 10px 30px rgba(0,0,0,0.18);
    overflow: hidden;
  }
  .card--front { left: 45px; }
  .card--back { left: 615px; }

  /* faint tone-on-tone decoration */
  .tone-disc {
    position: absolute;
    border-radius: 50%;
    background: var(--tone-faint);
  }
  .card--front .tone-disc {
    width: 270px;
    height: 270px;
    right: -70px;
    bottom: -110px;
  }
  .card--back .tone-disc {
    width: 250px;
    height: 250px;
    left: 40px;
    top: 39px;
  }
  .tone-name {
    position: absolute;
    left: 310px;
    top: 120px;
    font-family: "Josefin Sans", sans-serif;
    font-weight: 400;
    font-size: 34px;
    line-height: 1.15;
    letter-spacing: 1px;
    text-transform: uppercase;
    color: var(--tone-faint);
    margin: 0;
  }

  .brand {
    position: absolute;
    top: 44px;
    left: 60px;
    display: flex;
    align-items: center;
    gap: 12px;
  }
  .brand__dot {
    width: 46px;
    height: 46px;
    border-radius: 50%;
    background: var(--silver);
    flex: none;
  }
  .brand__text {
    display: flex;
    flex-direction: column;
  }
  .brand__name {
    font-family: "Josefin Sans", sans-serif;
    font-weight: 400;
    font-size: 27px;
    letter-spacing: 0.5px;
    text-transform: uppercase;
    color: var(--gold);
    line-height: 1;
    padding-bottom: 5px;
    border-bottom: 1px solid var(--gold);
  }
  .brand__sub {
    font-family: "Josefin Sans", sans-serif;
    font-weight: 400;
    font-size: 8px;
    letter-spacing: 1.5px;
    text-transform: uppercase;
    color: var(--gold);
    text-align: center;
    margin-top: 4px;
  }

  .contact {
    position: absolute;
    top: 150px;
    left: 0;
    width: 440px;
    text-align: center;
    font-family: "Tinos", serif;
    color: var(--white);
  }
  .contact__name {
    font-weight: 700;
    font-size: 17px;
    margin: 0 0 22px;
  }
  .contact__line {
    font-weight: 700;
    font-size: 11px;
    line-height: 1.45;
    margin: 0;
  }
</style>
</head>
<body>
<main class="canvas">
  <section class="card card--front" aria-label="Business card front">
    <span class="tone-disc" aria-hidden="true"></span>
    <div class="brand">
      <span class="brand__dot"></span>
      <div class="brand__text">
        <span class="brand__name">The Kestrel Vault</span>
        <span class="brand__sub">Construction Co.</span>
      </div>
    </div>
    <div class="contact">
      <p class="contact__name">Liam Porter</p>
      <p class="contact__line">Ph. 0427391065</p>
      <p class="contact__line">e-mail: Liam@thekestrelvault.com.au</p>
      <p class="contact__line">Builder Lic 517904k</p>
    </div>
  </section>
  <section class="card card--back" aria-label="Business card back">
    <span class="tone-disc" aria-hidden="true"></span>
    <p class="tone-name">The Kestrel<br>Vault</p>
  </section>
</main>
</body>
</html>
```